Lumen Path Tri-Fold Brochure - Recovering From Alzheimer's

Design a brochure a brochure for Lumen Path. www.lumenpath.org. We help people with Alzheimer's, or who have had a Traumatic Brain Injury, Concussion or Stroke stop their cognitive decline, and actually reverse decline and improve their cognitive abilities. We use an individualized approach, utilizing extensive lab work and developing a roadmap that includes diet, supplementation, theraputic devices all guided by a Memory Coach. I would like to see a design with pictures of people similar to the demographic on the website. Also incorporate some of the colors from my logo. We offer hope to people who consistently hear, "There is nothing we can do. Alzheimer's is a fatal disease." NOT TRUE! We see people's lives change every day!!!!

Target Market(s)

People who ARE or know someone suffering from cognitive decline, Alzheimer's, Traumatic Brain Injury, Concussion or Stroke.

Industry/Entity Type

Health and wellbeing -- Treating Alzheimer's.

Font styles to use
Other font styles liked:
• Calibri or I think it's called Lota

Colors
0054AA
0677BA
7BADD7
CADEEF
E8F1F8
0094D4
00A9DD
6FCCEA
C7EBF8
E9F6FB
00AB8E
00BBA5
67D7C9
C6EFE9
E9F9F6

Requirements
Must have
• Easily read material (think older eyes) and people between the ages of 40-70. Needs to have a professional feel but not clinical. Create trust and a feeling of caring and hope.
Nice to have
• Please check out my website: www.lumenpath.org for content and feel.
Should not have
• Youthful people exercising OR highly stereotypical ageist photos or info.

```html
<!DOCTYPE html>
<html lang="en">
<head>
<meta charset="utf-8">
<title>Lumen Path Tri-Fold Brochure</title>
<link rel="stylesheet" href="https://fonts.googleapis.com/css2?family=Libre+Baskerville:wght@700&family=Cormorant+Garamond:wght@500&family=Dancing+Script:wght@500&family=Roboto:ital,wght@0,400;1,400&display=swap">
<style>
  :root {
    --page: #d9d9d9;
    --white: #ffffff;
    --blue: #1a6fbf;
    --blue-deep: #0f5fae;
    --blue-head: #1b6ab4;
    --blue-light: #3fb0ea;
    --green: #0f9347;
    --green-light: #6cc04a;
    --green-text: #0e8a3e;
    --ink: #222222;
  }
  * { box-sizing: border-box; margin: 0; padding: 0; }
  html, body { width: 1022px; height: 1200px; overflow: hidden; background: var(--page); }
  .sheet {
    position: absolute; left: 21px; top: 254px;
    width: 1071px; height: 756px;
    transform: scale(0.915); transform-origin: top left;
    background: var(--white); overflow: hidden;
    box-shadow: 0 6px 18px rgba(0,0,0,0.18);
    font-family: "Roboto", Arial, sans-serif; color: var(--ink);
  }
  .abs { position: absolute; }
  .photo-landscape { left: 0; top: 0; width: 357px; height: 470px;
    background: linear-gradient(180deg, #2e74c4 0%, #6f8fb4 30%, #a7b3c1 55%, #ffffff 100%); }
  .photo-couple { left: 0; top: 470px; width: 357px; height: 286px;
    background: linear-gradient(180deg, #ffffff 0%, #e7e0d6 25%, #d9c7b3 55%, #bfae9c 100%); }
  .blue-panel { left: 714px; top: 160px; width: 357px; height: 560px; background: var(--blue); }
  .photo-family { left: 714px; top: 178px; width: 357px; height: 250px;
    background: linear-gradient(180deg, #5b6f86 0%, #8c7a6a 40%, #5d7fa8 75%, rgba(26,111,191,0) 100%); }
  .waves { left: 0; top: 0; width: 1071px; height: 756px; }
  .intro-box { left: 22px; top: 78px; width: 312px; height: 250px;
    background: linear-gradient(180deg, rgba(255,255,255,0.88) 0%, rgba(255,255,255,0.75) 70%, rgba(255,255,255,0) 100%);
    padding: 26px 22px 0; }
  .intro-text { font-size: 12.3px; line-height: 16.6px; text-align: justify; }
  .serif-head { font-family: "Libre Baskerville", Georgia, serif; font-weight: 700; text-transform: uppercase; text-align: center; }
  .left-head { left: 0; top: 332px; width: 357px; color: var(--green-text); font-size: 23px; line-height: 34px; }
  .mid-head { left: 714px; left: 357px; top: 38px; width: 357px; color: var(--blue-head); font-size: 21px; line-height: 30px; }
  .benefits { left: 382px; top: 120px; list-style: none; font-size: 11.4px; }
  .benefits li { display: flex; align-items: center; height: 25.5px; }
  .benefits svg { width: 10px; height: 10px; margin-right: 14px; }
  .statement { left: 380px; top: 284px; width: 330px; font-family: "Cormorant Garamond", Georgia, serif; font-weight: 500; font-size: 21px; line-height: 24px; text-transform: uppercase; letter-spacing: -0.2px; }
  .mid-brand { left: 357px; top: 352px; width: 357px; color: var(--blue-head); font-size: 20px; }
  .tagline { left: 357px; top: 385px; width: 357px; text-align: center; font-family: "Dancing Script", cursive; font-size: 30px; }
  .brand-mark { display: flex; align-items: center; justify-content: center; gap: 8px; }
  .brand-mark .dot { width: 14px; height: 14px; border-radius: 50%; background: var(--blue-head); }
  .mid-mark { left: 357px; top: 520px; width: 357px; color: var(--blue-head); font-family: "Libre Baskerville", Georgia, serif; font-weight: 700; font-size: 15px; }
  .contact { left: 382px; top: 628px; list-style: none; color: var(--white); font-size: 11.6px; line-height: 14px; }
  .contact li { display: flex; align-items: flex-start; margin-bottom: 12px; }
  .contact svg { width: 9px; height: 9px; margin: 2px 14px 0 0; fill: var(--white); }
  .right-brand { left: 714px; top: 60px; width: 357px; flex-direction: column; gap: 14px; color: var(--green-text); font-family: "Libre Baskerville", Georgia, serif; font-weight: 700; font-size: 21px; }
  .right-brand .dot { width: 52px; height: 52px; background: var(--blue-head); }
  .hero { left: 714px; top: 378px; width: 357px; color: var(--white); font-size: 46px; line-height: 46px; }
  .hero-sub { left: 714px; top: 562px; width: 357px; text-align: center; color: var(--white); font-style: italic; font-size: 22px; line-height: 30px; }
  .url { left: 714px; top: 706px; width: 357px; text-align: center; color: var(--white); font-size: 14px; }
</style>
</head>
<body>
<main class="sheet">
  <div class="abs photo-landscape" role="img" aria-label="Soft landscape photo of bare trees under a blue sky"></div>
  <div class="abs photo-couple" role="img" aria-label="Photo of a smiling older couple embracing at home"></div>
  <div class="abs blue-panel"></div>
  <div class="abs photo-family" role="img" aria-label="Photo of a grandfather laughing with his granddaughter in the kitchen"></div>

  <svg class="abs waves" viewBox="0 0 1071 756" aria-hidden="true">
    <path d="M714 180 C 850 190, 980 184, 1071 152 L1071 164 C 980 192, 850 198, 714 190 Z" fill="var(--blue-light)"/>
    <path d="M714 160 L1071 160 L1071 154 C 980 186, 850 192, 714 182 Z" fill="var(--white)"/>
    <path d="M714 648 C 850 690, 980 680, 1071 628 L1071 650 C 980 700, 850 705, 714 668 Z" fill="var(--green-light)"/>
    <path d="M0 705 C 140 620, 290 560, 420 560 C 560 560, 640 640, 760 668 C 880 700, 990 690, 1071 646 L1071 756 L0 756 Z" fill="var(--green)"/>
    <path d="M0 705 C 140 620, 290 560, 357 558 L357 756 L0 756 Z" fill="#7fbf86" opacity="0.75"/>
  </svg>

  <div class="abs intro-box">
    <p class="intro-text">You may believe there is nothing you can do to prevent or treat cognitive decline and Alzheimer’s disease. Maybe the idea of a personalized plan to prevent or reverse Alzheimer’s sounds like ‘snake oil’ or wishful thinking. Lumen Path can show you reputable science has opened new doors and created an unprecedented opportunity to change your brain health.</p>
  </div>
  <h2 class="abs serif-head left-head">You can change<br>your brain health</h2>

  <h2 class="abs serif-head mid-head">Join the brain health<br>revolution!</h2>
  <ul class="abs benefits">
    <li><svg viewBox="0 0 10 10"><path d="M1 9 L4 5 L9 1 L6 6 Z" fill="var(--green)"/></svg>Enhance Brain Function</li>
    <li><svg viewBox="0 0 10 10"><path d="M1 9 L4 5 L9 1 L6 6 Z" fill="var(--green)"/></svg>Do not settle – Optimize your Brain at any age</li>
    <li><svg viewBox="0 0 10 10"><path d="M1 9 L4 5 L9 1 L6 6 Z" fill="var(--green)"/></svg>Prevent Cognitive Decline</li>
    <li><svg viewBox="0 0 10 10"><path d="M1 9 L4 5 L9 1 L6 6 Z" fill="var(--green)"/></svg>Reverse Early Dementia</li>
    <li><svg viewBox="0 0 10 10"><path d="M1 9 L4 5 L9 1 L6 6 Z" fill="var(--green)"/></svg>Proven strategies can change your life and destiny</li>
  </ul>
  <p class="abs statement">Cognitive decline is not inevitable or normal aging!</p>
  <p class="abs serif-head mid-brand">Lumen Path</p>
  <p class="abs tagline">For Better Brain Health</p>
  <div class="abs brand-mark mid-mark"><span class="dot"></span>Lumen Path</div>
  <ul class="abs contact">
    <li><svg viewBox="0 0 10 10"><path d="M5 0 C2 0 1 2 1 4 C1 6 5 10 5 10 C5 10 9 6 9 4 C9 2 8 0 5 0 Z"/></svg>100 Harbor Lane<br>Fairview</li>
    <li><svg viewBox="0 0 10 10"><path d="M1 1 L3 0 L4.5 3 L3 4 C4 6 5 7 6 7 L7 5.5 L10 7 L9 9 C5 10 0 5 1 1 Z"/></svg>555-014-2290</li>
    <li><svg viewBox="0 0 10 10"><rect x="0" y="2" width="10" height="6"/></svg>info@lumenpath.org</li>
  </ul>

  <div class="abs brand-mark right-brand"><span class="dot"></span>LUMEN PATH</div>
  <h1 class="abs serif-head hero">Yes! Your<br>brain can<br>change!</h1>
  <p class="abs hero-sub">Lumen Path is here to<br>help!</p>
  <p class="abs url">www.lumenpath.org</p>
</main>
</body>
</html>
```